Dalton Power Supply, Inc. Business Card Design

We are an Electrical Distributor looking for a Modern, Professional Business Card design.

Target Market(s)

Residential Commercial Industrial

Industry/Entity Type

Electrical

Contact Information for Business Card

Dalton Power Supply, Inc.
418 Maple Ridge Lane
Brookvale, NC 27514
555-214-7630
555-214-8842 Fax
daltonpower@brightmail-example.net

```html
<!DOCTYPE html>
<html lang="en">
<head>
<meta charset="utf-8">
<title>Dalton Power Supply, Inc. — Business Card</title>
<link href="https://fonts.googleapis.com/css2?family=Mulish:wght@700;800&display=swap" rel="stylesheet">
<style>
  :root {
    --card-white: #ffffff;
    --brand-blue: #00339a;
    --brand-orange: #f7941d;
  }
  * { margin: 0; padding: 0; box-sizing: border-box; }
  html, body { width: 1200px; height: 732px; overflow: hidden; background: var(--card-white); }
  .business-card {
    position: relative;
    width: 1200px;
    height: 732px;
    background: var(--card-white);
    font-family: "Mulish", "Century Gothic", sans-serif;
    font-weight: 700;
    color: var(--brand-orange);
  }
  .company-name {
    position: absolute;
    top: 235px;
    left: 0;
    width: 100%;
    text-align: center;
    font-size: 64px;
    font-weight: 800;
    letter-spacing: 1px;
    color: var(--brand-blue);
    text-transform: uppercase;
  }
  .contact-band {
    position: absolute;
    left: 0;
    top: 425px;
    width: 100%;
    height: 166px;
    background: var(--brand-blue);
  }
  .address {
    position: absolute;
    left: 120px;
    top: 28px;
    font-size: 38px;
    line-height: 61px;
  }
  .address-pin {
    position: absolute;
    left: 68px;
    top: 54px;
    width: 36px;
    height: 60px;
  }
  .phones {
    position: absolute;
    right: 65px;
    top: 28px;
    font-size: 38px;
    line-height: 61px;
  }
  .phone-line { display: flex; align-items: center; justify-content: flex-end; gap: 16px; }
  .phone-line svg { width: 42px; height: 42px; }
  .email-band {
    position: absolute;
    left: 0;
    top: 628px;
    width: 100%;
    height: 52px;
    background: var(--brand-blue);
    text-align: center;
    font-size: 37px;
    line-height: 50px;
  }
</style>
</head>
<body>
  <div class="business-card">
    <h1 class="company-name">Dalton Power Supply, Inc.</h1>

    <div class="contact-band">
      <svg class="address-pin" viewBox="0 0 36 60" aria-hidden="true">
        <path d="M18 2 C8 2 2 9 2 18 C2 30 18 46 18 46 C18 46 34 30 34 18 C34 9 28 2 18 2 Z M18 11 a7 7 0 1 1 0 14 a7 7 0 1 1 0 -14 Z" fill="var(--brand-orange)" fill-rule="evenodd"/>
        <path d="M22 46 L34 58" stroke="var(--brand-orange)" stroke-width="5" stroke-linecap="round"/>
      </svg>
      <div class="address">
        <div>418 Maple Ridge Lane</div>
        <div>Brookvale, NC 27514</div>
      </div>
      <div class="phones">
        <div class="phone-line">
          <span>555-214-7630</span>
          <svg viewBox="0 0 42 42" aria-label="Phone" role="img">
            <rect x="3" y="3" width="36" height="36" fill="none" stroke="var(--brand-orange)" stroke-width="4"/>
            <path d="M13 10 L17 10 L19 16 L16 18 C17.5 22 20 24.5 24 26 L26 23 L32 25 L32 29 C32 31 30 32 28 32 C18 31 11 24 10 14 C10 12 11 10 13 10 Z" fill="var(--brand-orange)"/>
          </svg>
        </div>
        <div class="phone-line">
          <span>555-214-8842</span>
          <svg viewBox="0 0 42 42" aria-label="Fax" role="img">
            <rect x="11" y="3" width="20" height="10" fill="var(--brand-orange)"/>
            <rect x="2" y="13" width="38" height="18" rx="4" fill="var(--brand-orange)"/>
            <rect x="10" y="24" width="22" height="16" fill="var(--brand-blue)" stroke="var(--brand-orange)" stroke-width="3"/>
            <path d="M14 30 H28 M14 35 H28" stroke="var(--brand-orange)" stroke-width="2.5"/>
          </svg>
        </div>
      </div>
    </div>

    <div class="email-band">daltonpower@brightmail-example.net</div>
  </div>
</body>
</html>
```